CuraNex System Web Page Design

This project is to design 6 pages of a web based medical system for clinics, hospitals, drugs suppliers, general items suppliers, insurance company, laboratories and patients (basically all parties which could be involved in).We want the designs of the browser, button, icon and layout are based on Vex, which is user friendly, looks professional, simple and neat but with powerful functions. We have uploaded few pictures of another system, please do not copy its design because this is not what we are looking for, the pictures are for you to know the elements should be included in our pages. CuraNex web-base system, design 6 pages1. Login PageShould include the following elements-company id with input field-login id with input field-password with input field2. Main Page (Navigation page)Should include the following elements-Appointment-Consultation-Patient-Drugs inventory -General supplies inventory -Laboratory-Suppliers-Insurance-Reports 3. Appointment PageShould include all the the elements in the respective pictures plus the followings-Daily View, Weekly View, Monthly View buttons4. Consultation PageShould include all the the elements in the respective picture5. Patient Page5.1 General information Should include all the the elements in the respective picture5.2 medical history/lab reportsShould include all the the elements in the respective picture plus the followings-Notify patient button-Share report button.
Updated on 28 Nov:
Please stop using Ward Keystone in your designs which is not the name of our system. We have just rename our system to CuraNex, please take note.
We need the system to look professional not playful, do not use too many colors and playful icons.
professional users

```html
<!DOCTYPE html>
<html lang="en">
<head>
<meta charset="utf-8">
<title>CuraNex – Patient</title>
<link href="https://fonts.googleapis.com/css2?family=Roboto:wght@300;400;500;700&display=swap" rel="stylesheet">
<style>
:root{
  --blue:#1f5fae;
  --sidebar-bg:#e9ebef;
  --sidebar-text:#4b5563;
  --divider:#d3d6dc;
  --page-bg:#f7f7f8;
  --field-bg:#ffffff;
  --field-border:#d4d6da;
  --placeholder:#8b8d91;
  --label:#3c3c3c;
  --header-line:#c9cbcf;
}
*{box-sizing:border-box;margin:0;padding:0}
html,body{width:1200px;height:1066px;overflow:hidden}
body{position:relative;background:var(--page-bg);font-family:"Roboto",Arial,sans-serif}
.app-header{position:absolute;left:0;top:0;width:1200px;height:81px;background:#fff;border-bottom:1px solid var(--header-line)}
.brand{position:absolute;left:22px;top:22px;font-size:27px;font-weight:500;color:var(--blue);letter-spacing:.2px}
.user-menu{position:absolute;right:40px;top:12px;display:flex;align-items:center}
.user-avatar{width:57px;height:57px;border-radius:50%;background:linear-gradient(135deg,#c9ced6,#8b96a6);border:2px solid #e4e6ea}
.user-name{margin-left:14px;font-size:17px;color:#222}
.user-menu svg{margin-left:32px}
.sidebar{position:absolute;left:0;top:81px;width:209px;height:985px;background:var(--sidebar-bg);border-right:1px solid var(--divider)}
.nav-item{position:absolute;left:2px;width:206px;padding-left:31px;font-size:16px;font-weight:700;color:var(--sidebar-text);border-bottom:1px solid var(--divider);display:flex;align-items:center;line-height:19px}
.nav-item.active{background:var(--blue);color:#fff;border-bottom-color:var(--blue)}
.field{position:absolute;height:37px;background:var(--field-bg);border:1px solid var(--field-border);border-radius:4px;font-size:15px;font-weight:300;color:var(--placeholder);padding:8px 9px}
.field.tall{padding-top:10px}
.field .chev{position:absolute;right:10px;top:13px}
.field .cal{position:absolute;right:11px;top:8px}
.gender-label{position:absolute;left:725px;top:125px;font-size:15px;font-weight:300;color:var(--label)}
.radio{position:absolute;top:122px;width:21px;height:21px;border-radius:50%;border:1px solid #cfd1d5;background:#fff}
.radio.checked::after{content:"";position:absolute;left:7px;top:7px;width:5px;height:5px;border-radius:50%;background:var(--blue)}
.radio-label{position:absolute;top:125px;font-size:15px;font-weight:300;color:var(--label)}
.icon-btn{position:absolute;top:722px;width:37px;height:37px;border-radius:4px;display:flex;align-items:center;justify-content:center}
.icon-btn.add{left:1074px;background:var(--blue)}
.icon-btn.remove{left:1116px;background:#fff;border:1px solid var(--field-border)}
.action{position:absolute;top:992px;height:36px;border:1.5px solid var(--blue);border-radius:4px;background:#fff;color:var(--blue);font-size:15px;display:flex;align-items:center;justify-content:center}
</style>
</head>
<body>
<header class="app-header">
  <div class="brand">CuraNex</div>
  <div class="user-menu">
    <div class="user-avatar" role="img" aria-label="User profile photo"></div>
    <span class="user-name">Daniel Hart</span>
    <svg width="16" height="10" viewBox="0 0 16 10"><path d="M1.5 1.5 8 8l6.5-6.5" fill="none" stroke="#1f5fae" stroke-width="2.5"/></svg>
  </div>
</header>

<nav class="sidebar">
  <div class="nav-item" style="top:19px;height:43px">Appointments</div>
  <div class="nav-item" style="top:62px;height:32px">Consultation</div>
  <div class="nav-item active" style="top:94px;height:30px">Patient</div>
  <div class="nav-item" style="top:124px;height:31px">Drugs inventory</div>
  <div class="nav-item" style="top:155px;height:50px">General supplies<br>inventory</div>
  <div class="nav-item" style="top:205px;height:31px">Laboratory</div>
  <div class="nav-item" style="top:236px;height:31px">Suppliers</div>
  <div class="nav-item" style="top:267px;height:31px">Insurance</div>
  <div class="nav-item" style="top:298px;height:32px">Reports</div>
</nav>

<main>
  <div class="field" style="left:250px;top:117px;width:426px">Patient Code</div>
  <div class="field" style="left:250px;top:163px;width:426px">English Name</div>
  <div class="field" style="left:250px;top:210px;width:426px">Chinese Name</div>
  <div class="field" style="left:250px;top:254px;width:426px">H.K.I.D</div>
  <div class="field" style="left:250px;top:299px;width:426px">D.O.B
    <svg class="cal" width="22" height="20" viewBox="0 0 22 20"><rect x="1" y="3" width="20" height="16" rx="1.5" fill="none" stroke="#1f5fae" stroke-width="1.3"/><path d="M1 7h20M6 1v4M16 1v4" stroke="#1f5fae" stroke-width="1.3"/><path d="M4 10h2M8 10h2M12 10h2M16 10h2M4 13h2M8 13h2M12 13h2M16 13h2M4 16h2M8 16h2M12 16h2" stroke="#1f5fae" stroke-width="1.2"/></svg>
  </div>
  <div class="field" style="left:250px;top:346px;width:426px">Mobile No</div>
  <div class="field tall" style="left:250px;top:390px;width:426px;height:94px">Res Address</div>
  <div class="field" style="left:250px;top:493px;width:426px">Res District.<svg class="chev" width="16" height="10" viewBox="0 0 16 10"><path d="M1.5 1.5 8 8l6.5-6.5" fill="none" stroke="#1f5fae" stroke-width="2.5"/></svg></div>
  <div class="field" style="left:250px;top:538px;width:426px">Res Area<svg class="chev" width="16" height="10" viewBox="0 0 16 10"><path d="M1.5 1.5 8 8l6.5-6.5" fill="none" stroke="#1f5fae" stroke-width="2.5"/></svg></div>
  <div class="field" style="left:250px;top:582px;width:426px">Occupdation<svg class="chev" width="16" height="10" viewBox="0 0 16 10"><path d="M1.5 1.5 8 8l6.5-6.5" fill="none" stroke="#1f5fae" stroke-width="2.5"/></svg></div>
  <div class="field" style="left:250px;top:628px;width:426px">Contract<svg class="chev" width="16" height="10" viewBox="0 0 16 10"><path d="M1.5 1.5 8 8l6.5-6.5" fill="none" stroke="#1f5fae" stroke-width="2.5"/></svg></div>
  <div class="field" style="left:250px;top:674px;width:426px">Insurance No.</div>
  <div class="field tall" style="left:250px;top:718px;width:426px;height:114px">Insurance Plan.</div>
  <div class="field tall" style="left:250px;top:841px;width:426px;height:114px">Remarks</div>

  <span class="gender-label">Gender</span>
  <span class="radio checked" style="left:931px"></span>
  <span class="radio-label" style="left:967px">Male</span>
  <span class="radio" style="left:1048px"></span>
  <span class="radio-label" style="left:1091px">Female</span>

  <div class="field" style="left:903px;top:164px;width:250px">Prefix<svg class="chev" width="16" height="10" viewBox="0 0 16 10"><path d="M1.5 1.5 8 8l6.5-6.5" fill="none" stroke="#1f5fae" stroke-width="2.5"/></svg></div>
  <div class="field" style="left:727px;top:210px;width:426px">Blood Type<svg class="chev" width="16" height="10" viewBox="0 0 16 10"><path d="M1.5 1.5 8 8l6.5-6.5" fill="none" stroke="#1f5fae" stroke-width="2.5"/></svg></div>
  <div class="field" style="left:727px;top:254px;width:426px">Telephone</div>
  <div class="field tall" style="left:727px;top:299px;width:426px;height:81px">Bus. Address</div>
  <div class="field" style="left:727px;top:390px;width:426px">Bus. District<svg class="chev" width="16" height="10" viewBox="0 0 16 10"><path d="M1.5 1.5 8 8l6.5-6.5" fill="none" stroke="#1f5fae" stroke-width="2.5"/></svg></div>
  <div class="field" style="left:727px;top:434px;width:426px">Dr. In Charge<svg class="chev" width="16" height="10" viewBox="0 0 16 10"><path d="M1.5 1.5 8 8l6.5-6.5" fill="none" stroke="#1f5fae" stroke-width="2.5"/></svg></div>
  <div class="field" style="left:727px;top:481px;width:426px">Reffered By<svg class="chev" width="16" height="10" viewBox="0 0 16 10"><path d="M1.5 1.5 8 8l6.5-6.5" fill="none" stroke="#1f5fae" stroke-width="2.5"/></svg></div>
  <div class="field" style="left:727px;top:526px;width:426px">Email</div>
  <div class="field tall" style="left:727px;top:570px;width:426px;height:142px">Family History</div>
  <div class="field" style="left:727px;top:722px;width:329px">Group<svg class="chev" width="16" height="10" viewBox="0 0 16 10"><path d="M1.5 1.5 8 8l6.5-6.5" fill="none" stroke="#1f5fae" stroke-width="2.5"/></svg></div>
  <div class="icon-btn add"><svg width="17" height="17" viewBox="0 0 17 17"><path d="M8.5 1v15M1 8.5h15" stroke="#fff" stroke-width="2"/></svg></div>
  <div class="icon-btn remove"><svg width="15" height="2" viewBox="0 0 15 2"><path d="M0 1h15" stroke="#c9cbcf" stroke-width="1.5"/></svg></div>
  <div class="field" style="left:727px;top:766px;width:426px;height:187px"></div>

  <div class="action" style="left:252px;width:104px">New</div>
  <div class="action" style="left:371px;width:110px">Save</div>
  <div class="action" style="left:498px;width:110px">Print Eng</div>
  <div class="action" style="left:624px;width:110px">Print Chin</div>
  <div class="action" style="left:749px;width:110px">Patient Chart</div>
  <div class="action" style="left:872px;width:110px">Main</div>
</main>
</body>
</html>
```